Quorvane Limited needs a business card design

We need a business card design that reflects both professionalism and innovation and captures our brand identity. We provide online enterprise solutions to HR and executive management. We would like to use the colors in our logo (Blue and Orange). See attached file.

We would like a more creative design than the existing attached business card but maintain the same information on it.

To see our products site, please visit www.quorvane.example which reflects more our identity
Updates

Please see our site: www.quorvane.example, not www.quorvane.example.uk for our colors and look and feel

Target Market(s)

Senior Executives

Industry/Entity Type

Business

Requirements
Must have
• Logo and use of logo colors
Nice to have
• Icons
Should not have
• Images

```html
<!DOCTYPE html>
<html lang="en">
<head>
<meta charset="utf-8">
<title>Quorvane Limited – Business Card</title>
<link rel="stylesheet" href="https://fonts.googleapis.com/css2?family=Exo+2:wght@400;600;700&display=swap">
<style>
  :root{
    --brand-blue:#1f4fcf;
    --brand-orange:#e8561c;
    --ink:#2b2b2b;
    --card:#ffffff;
    --panel:#efefef;
    --rule:#9a9a9a;
    --backdrop:#d6d6d6;
  }
  *{box-sizing:border-box;margin:0;padding:0}
  html,body{width:1200px;height:949px;overflow:hidden}
  body{background:var(--backdrop);font-family:"Exo 2",Arial,sans-serif;color:var(--ink);position:relative}
  .card{position:absolute;top:184px;width:340px;height:580px;background:var(--card);border-radius:18px;overflow:hidden;box-shadow:0 10px 24px rgba(0,0,0,.18)}
  .card--back{left:220px}
  .card--front{left:640px}

  .wordmark{font-weight:700;color:var(--brand-blue);letter-spacing:-1px;line-height:1}
  .card--back .wordmark{position:absolute;left:0;right:0;top:250px;text-align:center;font-size:58px}
  .back-band{position:absolute;left:0;right:0;bottom:0;height:14px;background:var(--brand-blue)}
  .social{position:absolute;right:22px;bottom:32px;display:flex;gap:12px}
  .social span{width:14px;height:14px;border-radius:50%;background:var(--brand-orange);display:block}

  .card--front .wordmark{position:absolute;left:30px;top:48px;font-size:52px}
  .identity{position:absolute;left:30px;top:140px;display:flex;align-items:center;gap:8px;font-size:15px;letter-spacing:1px}
  .identity .name{font-weight:600}
  .identity .role{margin-left:22px;font-size:14px}
  .contact-list{position:absolute;left:0;right:0;top:190px;bottom:0;background:var(--panel);list-style:none}
  .contact-list::before{content:"";position:absolute;left:0;top:20px;bottom:60px;width:22px;background:var(--brand-blue)}
  .contact-item{position:relative;height:82px;display:flex;align-items:center;gap:16px;padding-left:40px;border-bottom:1px solid var(--rule);font-size:16px;letter-spacing:.5px}
  .contact-item:last-child{border-bottom:none;height:auto;padding-top:18px;align-items:flex-start}
  .contact-item.web{font-size:13px}
  .contact-item svg{flex:none;width:24px;height:24px;fill:var(--brand-orange)}
</style>
</head>
<body>
  <section class="card card--back" aria-label="Card back">
    <div class="wordmark">Quorvane</div>
    <div class="social" aria-label="Social links"><span></span><span></span><span></span></div>
    <div class="back-band"></div>
  </section>

  <section class="card card--front" aria-label="Card front">
    <div class="wordmark">Quorvane</div>
    <div class="identity">
      <svg width="14" height="16" viewBox="0 0 14 16" aria-hidden="true"><circle cx="7" cy="4" r="3.5" fill="var(--brand-orange)"/><path d="M0 16a7 6 0 0 1 14 0z" fill="var(--brand-orange)"/></svg>
      <span class="name">MARA ELLISON</span>
      <span class="role">founder</span>
    </div>
    <ul class="contact-list">
      <li class="contact-item">
        <svg viewBox="0 0 24 24" aria-hidden="true"><path d="M6.6 10.8a15 15 0 0 0 6.6 6.6l2.2-2.2a1 1 0 0 1 1-.25 11.4 11.4 0 0 0 3.6.6 1 1 0 0 1 1 1V20a1 1 0 0 1-1 1A17 17 0 0 1 3 4a1 1 0 0 1 1-1h3.5a1 1 0 0 1 1 1c0 1.25.2 2.45.6 3.6a1 1 0 0 1-.25 1z"/></svg>
        <span>012 555 0148</span>
      </li>
      <li class="contact-item">
        <svg viewBox="0 0 24 24" aria-hidden="true"><path d="M2 5h20v14H2z"/><path d="M2 5l10 8 10-8" fill="none" stroke="#fff" stroke-width="1.6"/></svg>
        <span>mara@quorvane.example</span>
      </li>
      <li class="contact-item web">
        <svg viewBox="0 0 24 24" aria-hidden="true"><circle cx="12" cy="12" r="10"/><g fill="none" stroke="#fff" stroke-width="1.2"><ellipse cx="12" cy="12" rx="4.5" ry="10"/><path d="M2 12h20M4 7h16M4 17h16M12 2v20"/></g></svg>
        <span>www.quorvane.example</span>
      </li>
      <li class="contact-item">
        <svg viewBox="0 0 24 24" aria-hidden="true"><path d="M12 2a7 7 0 0 0-7 7c0 5 7 13 7 13s7-8 7-13a7 7 0 0 0-7-7zm0 9.5A2.5 2.5 0 1 1 12 6.5a2.5 2.5 0 0 1 0 5z"/></svg>
        <span>214, 6th Floor, Arden Plaza<br>Linden Road NRB</span>
      </li>
    </ul>
  </section>
</body>
</html>
```